Used Car Dealer seeks an Amazing Business Card Design

We are looking for a business card design that incorporates our logo and grabs the attention of anyone we give the business card to.

Looking to use the same colors as the logo. Our Logo choice is the black background with Red and Silver/Grey Lettering.

We also would like to see some embossed designs.

Target Market(s)

Used Car Buyers, Automotive, Auto

Industry/Entity Type

Automotive

Contact Information for Business Card

BVEL7K
Gordon Whitlock
482 Tarrow Lane
Suite 207
Larkfield, GA 30991
Office (770) 555-0142
Cell (770) 555-0187
bvel7kga@quellmail.com
www.bvel7kga.com

Colors
ffffff
ee3036

Requirements
Must have
• Must include our logo (Black Background with Red and Silver/Grey Lettering)
Nice to have
• Embossed Design. Can be Single or Double Sided.

```html
<!DOCTYPE html>
<html lang="en">
<head>
<meta charset="utf-8">
<title>BVEL7K Business Card</title>
<link href="https://fonts.googleapis.com/css2?family=Lato:wght@400;700;900&display=swap" rel="stylesheet">
<style>
  :root {
    --backdrop: #e9e6e1;
    --card-black: #0c0c0d;
    --card-grey: #2b2b2e;
    --accent-red: #ee3036;
    --silver: #d9d9d9;
    --white: #ffffff;
    --soft-white: #e6e6e6;
  }
  * { margin: 0; padding: 0; box-sizing: border-box; }
  html, body { width: 1200px; height: 780px; overflow: hidden; }
  body {
    background: var(--backdrop);
    font-family: "Lato", Arial, sans-serif;
    display: flex;
    align-items: center;
    justify-content: center;
    gap: 40px;
  }
  .card {
    position: relative;
    width: 560px;
    height: 320px;
    border-radius: 14px;
    overflow: hidden;
    box-shadow: 0 10px 30px rgba(0,0,0,0.25);
  }
  .card-back { background: var(--card-grey); }
  .card-front { background: var(--card-black); display: flex; align-items: center; justify-content: center; }
  .back-shape { position: absolute; inset: 0; }
  .wordmark {
    font-weight: 900;
    color: var(--silver);
    letter-spacing: 2px;
    display: flex;
    align-items: center;
    gap: 12px;
    line-height: 1;
  }
  .wordmark-dot { border-radius: 50%; background: var(--accent-red); flex: none; }
  .card-back .wordmark { position: absolute; top: 48px; right: 40px; font-size: 40px; }
  .card-back .wordmark-dot { width: 16px; height: 16px; }
  .card-front .wordmark { font-size: 76px; }
  .card-front .wordmark-dot { width: 28px; height: 28px; }
  .contact { position: absolute; left: 44px; bottom: 28px; color: var(--white); }
  .person-name { font-weight: 900; font-size: 21px; letter-spacing: 1px; text-transform: uppercase; line-height: 1.2; }
  .person-title { color: var(--accent-red); font-size: 15px; margin-bottom: 12px; }
  .address { font-size: 14px; line-height: 1.4; margin-bottom: 10px; color: var(--soft-white); }
  .details { list-style: none; font-size: 14px; line-height: 1.55; color: var(--soft-white); }
  .details li { display: flex; align-items: center; gap: 8px; }
  .icon {
    width: 16px; height: 16px; border-radius: 3px;
    background: var(--accent-red);
    display: inline-flex; align-items: center; justify-content: center;
    flex: none;
  }
  .edge-tab {
    position: absolute; left: -16px; bottom: 36px;
    width: 32px; height: 32px; border-radius: 50%;
    background: var(--accent-red);
  }
</style>
</head>
<body>
  <section class="card card-back">
    <svg class="back-shape" viewBox="0 0 560 320" width="560" height="320">
      <path d="M150 0 Q 300 215 560 235 L560 0 Z" fill="var(--card-black)"/>
      <path d="M150 0 Q 300 215 560 235" fill="none" stroke="var(--accent-red)" stroke-width="4"/>
    </svg>
    <div class="wordmark"><span class="wordmark-dot"></span>BVEL7K</div>
    <span class="edge-tab"></span>
    <div class="contact">
      <p class="person-name">Gordon Whitlock</p>
      <p class="person-title">Director</p>
      <p class="address">482 Tarrow Lane<br>Suite 207<br>Larkfield, GA 30991</p>
      <ul class="details">
        <li><span class="icon"><svg width="10" height="10" viewBox="0 0 10 10"><path d="M2 1 L4 1 L4.5 3 L3.5 4 Q4.5 6 6 6.5 L7 5.5 L9 6 L9 8 Q5 9 1 3 Z" fill="#fff"/></svg></span>(770) 555-0142</li>
        <li><span class="icon"><svg width="10" height="10" viewBox="0 0 10 10"><rect x="3" y="1" width="4" height="8" rx="1" fill="none" stroke="#fff" stroke-width="1.2"/></svg></span>(770) 555-0187</li>
        <li><span class="icon"><svg width="10" height="10" viewBox="0 0 10 10"><rect x="1" y="2.5" width="8" height="5" fill="none" stroke="#fff" stroke-width="1.1"/><path d="M1 2.5 L5 5.5 L9 2.5" fill="none" stroke="#fff" stroke-width="1.1"/></svg></span>bvel7kga@quellmail.com</li>
        <li><span class="icon"><svg width="10" height="10" viewBox="0 0 10 10"><circle cx="5" cy="5" r="3.8" fill="none" stroke="#fff" stroke-width="1.1"/><path d="M1.2 5 H8.8 M5 1.2 V8.8" stroke="#fff" stroke-width="0.9"/></svg></span>www.bvel7kga.com</li>
      </ul>
    </div>
  </section>

  <section class="card card-front">
    <div class="wordmark"><span class="wordmark-dot"></span>BVEL7K</div>
  </section>
</body>
</html>
```